Ridgeline Yard Works Stationary Package
Business Cards, Letterhead, Envelope, Sticker, Fax Cover sheet, invoice, and estimate
Ridgeline Yard Works Stationary Package - Construction
Creative Brief
Use same font as used in my logo
Pete Marrow
Owner
4172 W. Fenwick Rd. Burbank, IL 60421
petemarrow@quailnet.example
www.ridgelineyardworks.example
Can information be in a format that can be edited for future use. ex: Name Changes, New Numbers, etc?

```html
<!DOCTYPE html>
<html lang="en">
<head>
<meta charset="utf-8">
<title>Ridgeline Yard Works – Business Card</title>
<link href="https://fonts.googleapis.com/css2?family=Arimo:wght@400;700&display=swap" rel="stylesheet">
<style>
  :root {
    --backdrop: #e9e6e1;
    --card: #ffffff;
    --navy: #1f2a5c;
    --navy-deep: #141d49;
    --glow: #2a7fc4;
    --red: #c8202b;
    --ink: #222222;
    --name-ink: #1d2540;
    --owner-ink: #c9d3ea;
  }
  html, body {
    margin: 0;
    padding: 0;
    width: 1200px;
    height: 778px;
    overflow: hidden;
    background: var(--backdrop);
  }
  .business-card {
    position: absolute;
    left: 117px;
    top: 49px;
    width: 966px;
    height: 680px;
    background: var(--card);
    overflow: hidden;
    box-shadow: 0 2px 10px rgba(0,0,0,0.15);
    font-family: "Arimo", Arial, sans-serif;
  }
  .swoosh {
    position: absolute;
    left: 0;
    top: 0;
    width: 966px;
    height: 680px;
  }
  .brand {
    position: absolute;
    left: 46px;
    top: 136px;
    display: flex;
    align-items: center;
    gap: 22px;
  }
  .brand-square {
    width: 100px;
    height: 100px;
    border-radius: 14px;
    background: var(--navy);
  }
  .brand-name {
    font-size: 44px;
    font-weight: 700;
    color: var(--name-ink);
    letter-spacing: -0.5px;
  }
  .address {
    position: absolute;
    left: 43px;
    top: 322px;
    font-size: 23px;
    line-height: 35px;
    color: var(--ink);
  }
  .contact-list {
    position: absolute;
    left: 43px;
    top: 402px;
    margin: 0;
    padding: 0;
    list-style: none;
    font-size: 22px;
    line-height: 35px;
    color: var(--ink);
  }
  .contact-list li {
    display: flex;
    align-items: center;
    gap: 12px;
  }
  .contact-icon {
    width: 18px;
    height: 18px;
    flex: none;
  }
  .holder {
    position: absolute;
    right: 40px;
    top: 528px;
    text-align: right;
    color: #ffffff;
  }
  .holder-name {
    font-size: 32px;
    font-weight: 400;
    line-height: 38px;
  }
  .holder-title {
    font-size: 22px;
    font-weight: 700;
    color: var(--owner-ink);
    line-height: 30px;
  }
</style>
</head>
<body>
  <div class="business-card">
    <svg class="swoosh" viewBox="0 0 966 680" aria-hidden="true">
      <defs>
        <radialGradient id="navyGlow" cx="520" cy="640" r="420" gradientUnits="userSpaceOnUse">
          <stop offset="0" stop-color="var(--glow)"/>
          <stop offset="0.55" stop-color="var(--navy)"/>
          <stop offset="1" stop-color="var(--navy-deep)"/>
        </radialGradient>
      </defs>
      <path class="swoosh-red" fill="var(--red)"
            d="M0,640 C320,600 640,480 966,290 L966,318 C640,500 320,622 0,660 Z"/>
      <path class="swoosh-navy" fill="url(#navyGlow)"
            d="M0,676 C320,640 650,520 966,336 L966,680 L0,680 Z"/>
    </svg>

    <div class="brand">
      <div class="brand-square"></div>
      <div class="brand-name">Ridgeline Yard Works</div>
    </div>

    <div class="address">
      4172 W. Fenwick Rd.<br>
      Burbank, IL 60421
    </div>

    <ul class="contact-list">
      <li>
        <svg class="contact-icon" viewBox="0 0 18 18" aria-hidden="true">
          <rect x="4" y="1" width="10" height="16" rx="2" fill="var(--red)"/>
          <rect x="6" y="4" width="6" height="7" fill="#fff"/>
        </svg>
        (708) 555-0142
      </li>
      <li>
        <svg class="contact-icon" viewBox="0 0 18 18" aria-hidden="true">
          <rect x="5" y="1" width="8" height="6" fill="var(--red)"/>
          <rect x="1" y="7" width="16" height="8" rx="1.5" fill="var(--red)"/>
          <rect x="5" y="12" width="8" height="5" fill="#fff" stroke="var(--red)" stroke-width="1.5"/>
        </svg>
        (708) 555-0187
      </li>
      <li>
        <svg class="contact-icon" viewBox="0 0 18 18" aria-hidden="true">
          <rect x="1" y="4" width="16" height="11" rx="1.5" fill="none" stroke="var(--red)" stroke-width="2"/>
          <path d="M1.5,5 L9,10.5 L16.5,5" fill="none" stroke="var(--red)" stroke-width="2"/>
        </svg>
        petemarrow@quailnet.example
      </li>
      <li>
        <svg class="contact-icon" viewBox="0 0 18 18" aria-hidden="true">
          <circle cx="9" cy="9" r="8" fill="var(--red)"/>
          <path d="M1,9 H17 M9,1 C5,5 5,13 9,17 M9,1 C13,5 13,13 9,17" fill="none" stroke="#fff" stroke-width="1.2"/>
        </svg>
        www.ridgelineyardworks.example
      </li>
    </ul>

    <div class="holder">
      <div class="holder-name">Pete Marrow</div>
      <div class="holder-title">Owner</div>
    </div>
  </div>
</body>
</html>
```